Tall Harbor Business Card

We are a Video Production and Video Equipment Rental company specialising in the supply of state of the art Video Technology and Services for the Live Entertainment, Television and Corporate Business Theatre markets. (in Sydney, Australia) www.tallharbor-media.example

Industry/Entity Type

Business

Contact Information for Business Card

name, position, email, website, address, logo
Example attached of the information we need - doesn't necessarily have to look the same

Font styles to use
Other font styles liked:
• Tall Harbor logo font is GOTHAM

Colors
ea1f27

Requirements
Nice to have
• either matt black or shiny black cards -
raised logo

```html
<!DOCTYPE html>
<html lang="en">
<head>
<meta charset="utf-8">
<title>Tall Harbor Business Card</title>
<link rel="stylesheet" href="https://fonts.googleapis.com/css2?family=Montserrat:wght@400;500;600;700&display=swap">
<style>
  :root {
    --brand-red: #ea1f27;
    --ink-black: #111111;
    --paper-light: #ecebea;
    --ink-grey: #3d3d3d;
    --white: #ffffff;
    --backdrop: #e4e4e4;
  }
  * { box-sizing: border-box; margin: 0; padding: 0; }
  html, body { width: 1200px; height: 777px; overflow: hidden; }
  body {
    background: var(--backdrop);
    font-family: "Montserrat", sans-serif;
    position: relative;
  }
  .card {
    position: absolute;
    top: 228px;
    width: 560px;
    height: 320px;
    overflow: hidden;
    box-shadow: 0 8px 24px rgba(0,0,0,0.18);
  }
  .card--front { left: 25px; --top: var(--paper-light); --logo: var(--ink-black); --name: var(--brand-red); --title: var(--ink-grey); --stripe: var(--ink-black); --tick: var(--white); --services: var(--ink-black); }
  .card--back { left: 615px; --top: var(--ink-black); --logo: var(--white); --name: var(--white); --title: var(--brand-red); --stripe: var(--white); --tick: var(--ink-black); --services: var(--white); }

  .card__upper { position: absolute; left: 0; right: 0; top: 0; height: 190px; background: var(--top); }
  .card__lower { position: absolute; left: 0; right: 0; top: 190px; bottom: 0; background: var(--brand-red); }

  .logo {
    position: absolute; top: 44px; left: 48px;
    display: flex; align-items: center; gap: 14px;
  }
  .logo__square { width: 16px; height: 16px; background: var(--brand-red); }
  .logo__name {
    font-size: 36px; font-weight: 600; letter-spacing: 1px;
    color: var(--logo); text-transform: uppercase; line-height: 44px;
  }

  .stripe { position: absolute; left: 330px; right: 0; height: 16px; background: var(--stripe); }
  .card--front .stripe { top: 168px; }
  .card--back .stripe { top: 276px; height: 12px; left: 400px; }
  .stripe__tick { position: absolute; top: 0; bottom: 0; width: 6px; background: var(--tick); }
  .stripe__tick--a { left: 100px; }
  .stripe__tick--b { left: 160px; }
  .card--back .stripe__tick--a { left: 70px; }
  .card--back .stripe__tick--b { left: 120px; }

  .person { position: absolute; left: 48px; top: 118px; }
  .person__name { font-size: 26px; font-weight: 700; color: var(--name); text-transform: uppercase; line-height: 30px; letter-spacing: 0.5px; }
  .person__title { font-size: 18px; font-weight: 400; color: var(--title); text-transform: uppercase; line-height: 24px; letter-spacing: 0.5px; }

  .rule { position: absolute; left: 0; right: 0; top: 184px; height: 6px; background: var(--ink-black); }

  .contact {
    position: absolute; left: 48px; top: 204px;
    font-size: 13px; font-weight: 500; color: var(--white);
    text-transform: uppercase; line-height: 18px; letter-spacing: 0.3px;
  }
  .contact__gap { height: 6px; }
  .services {
    position: absolute; left: 48px; bottom: 12px;
    font-size: 12px; font-weight: 500; line-height: 16px; color: var(--services);
    text-transform: uppercase; letter-spacing: 0.3px; white-space: nowrap;
  }
</style>
</head>
<body>

<section class="card card--front" aria-label="Business card, light side">
  <div class="card__upper"></div>
  <div class="card__lower"></div>
  <div class="rule"></div>
  <div class="stripe"><span class="stripe__tick stripe__tick--a"></span><span class="stripe__tick stripe__tick--b"></span></div>
  <div class="logo"><span class="logo__square"></span><span class="logo__name">Tall Harbor</span></div>
  <div class="person">
    <p class="person__name">Marco Delvecchio</p>
    <p class="person__title">Managing Director</p>
  </div>
  <div class="contact">
    <p>17 Keel Street, Harbourside NSW 2000</p>
    <p>Australia</p>
    <div class="contact__gap"></div>
    <p>marco@tallharbor-media.example</p>
    <p>www.tallharbor-media.example</p>
  </div>
  <p class="services">Video Solutions | LED Screens | Camera Systems | Projection</p>
</section>

<section class="card card--back" aria-label="Business card, black side">
  <div class="card__upper"></div>
  <div class="card__lower"></div>
  <div class="stripe"><span class="stripe__tick stripe__tick--a"></span><span class="stripe__tick stripe__tick--b"></span></div>
  <div class="logo"><span class="logo__square"></span><span class="logo__name">Tall Harbor</span></div>
  <div class="person">
    <p class="person__name">Marco Delvecchio</p>
    <p class="person__title">Managing Director</p>
  </div>
  <div class="contact">
    <p>17 Keel Street, Harbourside NSW 2000</p>
    <p>Australia</p>
    <div class="contact__gap"></div>
    <p>marco@tallharbor-media.example</p>
    <p>www.tallharbor-media.example</p>
  </div>
  <p class="services">Video Solutions | LED Screens | Camera Systems | Projection</p>
</section>

</body>
</html>
```